PLUMBING POSTCARD DESIGN (MARKETING)

We are a local Plumbing business , Needing a post card to market domestic plumbing maintenance in my local area. The post card will have a magnet business card attached so allowance in design will need to be made. I have a slogan i want Incorporated into the design and is "TRY THE BEST, FLUSH THE REST"
I have attached my company name and logo to also incorporate into the design.
post card size 21cm L x 10cm H
business magnet card that will be attached to post card is 9cm L X 5.5cm H.
Post card will be one sided and will need following text inserted into design:
Pipewell would like to offer its fellow locals $40 off their next plumbing job. We pride ourselves in supplying the highest level of workmanship at the most competitive prices. CALL US TODAY
0431 582 907
Target Market(s)
Property owners (domestic market0
Industry/Entity Type
Plumbing
Requirements
Must have
- Eye catching, Slogan, company name and logo

```html
<!DOCTYPE html>
<html lang="en">
<head>
<meta charset="utf-8">
<title>Pipewell Plumbing Postcard</title>
<link href="https://fonts.googleapis.com/css2?family=Montserrat:wght@500;600;700;800;900&family=Oswald:wght@500;600;700&display=swap" rel="stylesheet">
<style>
  :root{
    --blue:#1c9fd0;
    --blue-deep:#1a86b8;
    --orange:#f06a36;
    --orange-mid:#f39a35;
    --yellow:#f7c83e;
    --ink:#2b2b2b;
    --grey:#5a5a5a;
    --paper:#ffffff;
    --paper-soft:#f3f4f6;
    --stage:#e9eaec;
  }
  *{box-sizing:border-box;margin:0;padding:0}
  html,body{width:1200px;height:720px;overflow:hidden;background:var(--stage)}
  .postcard{position:absolute;left:40px;top:93px;width:1120px;height:533px;background:linear-gradient(135deg,var(--paper) 0%,var(--paper-soft) 100%);overflow:hidden;font-family:'Montserrat',sans-serif;box-shadow:0 6px 24px rgba(0,0,0,.12)}

  /* brand */
  .brand{position:absolute;left:48px;top:30px;display:flex;align-items:center;gap:12px}
  .brand-dot{width:44px;height:44px;border-radius:50%;background:var(--blue)}
  .brand-name{font-weight:800;font-size:34px;color:var(--ink);line-height:1;letter-spacing:.5px}
  .brand-tag{position:absolute;left:104px;top:76px;font-weight:500;font-size:14px;color:var(--grey);letter-spacing:.5px}

  /* contact pill */
  .contact{position:absolute;left:520px;top:44px;width:560px;height:40px;border-radius:20px;overflow:hidden;display:flex;color:#fff;font-weight:600;font-size:17px;white-space:nowrap}
  .contact-item{display:flex;align-items:center;gap:10px;padding:0 22px}
  .contact-email{background:var(--blue-deep);width:47%}
  .contact-web{background:linear-gradient(90deg,var(--orange),var(--orange-mid) 60%,var(--yellow));flex:1}
  .contact svg{width:18px;height:18px;flex:none}

  /* slogan */
  .slogan-band{position:absolute;left:0;top:104px;width:560px;height:134px;background:linear-gradient(90deg,var(--blue-deep),var(--blue))}
  .slogan{position:absolute;left:58px;top:116px;color:#fff;font-weight:900;font-size:50px;line-height:1.08;letter-spacing:.5px;white-space:nowrap}

  /* body copy */
  .intro{position:absolute;left:58px;top:248px;width:470px;font-size:14.5px;font-weight:500;line-height:1.5;color:var(--ink)}
  .intro .name{color:var(--blue-deep);font-weight:800}
  .intro .tag{display:inline-block;background:var(--orange);color:#fff;font-family:'Oswald',sans-serif;font-weight:600;font-size:13px;padding:0 8px;border:1px dashed var(--yellow);line-height:1.4}
  .intro .accent{color:var(--orange);font-weight:700}

  /* call block */
  .call-band{position:absolute;left:0;top:372px;width:560px;height:161px;background:linear-gradient(90deg,var(--orange),var(--orange-mid));clip-path:polygon(0 0,86% 0,100% 100%,0 100%)}
  .call-tab{position:absolute;left:48px;top:348px;background:var(--blue);color:#fff;font-weight:800;font-size:22px;padding:8px 20px;letter-spacing:.5px;white-space:nowrap}
  .call-number{position:absolute;left:44px;top:404px;display:flex;align-items:center;gap:14px;color:#fff;font-weight:900;font-size:56px;letter-spacing:1px;white-space:nowrap;line-height:1.1}
  .phone-ring{width:46px;height:46px;border-radius:50%;background:#fff;border:4px solid var(--blue);display:flex;align-items:center;justify-content:center;flex:none}
  .phone-ring svg{width:24px;height:24px}

  /* coupon */
  .coupon{position:absolute;left:566px;top:110px;width:514px;height:290px;border:2px dashed var(--orange);border-radius:20px;overflow:hidden;background:#fff}
  .coupon-photo{position:absolute;left:170px;top:0;width:344px;height:140px;background:linear-gradient(135deg,#d9dde2,#b9c2cc 55%,#8fa6c4)}
  .coupon-bar{position:absolute;left:0;top:190px;width:100%;height:100px;background:linear-gradient(90deg,var(--orange),var(--orange-mid) 50%,var(--yellow))}
  .coupon-offer{position:absolute;left:0;top:0;width:300px;height:290px;background:linear-gradient(160deg,var(--blue-deep),var(--blue));clip-path:polygon(0 0,100% 0,44% 100%,0 100%);color:#fff;font-family:'Oswald',sans-serif;padding:18px 0 0 28px}
  .offer-amount{font-weight:700;font-size:84px;line-height:1;white-space:nowrap}
  .offer-amount small{font-size:36px;vertical-align:top;margin-left:6px;position:relative;top:6px}
  .offer-line{font-weight:600;font-size:33px;line-height:1.08;margin-top:4px}
  .coupon-number{position:absolute;left:204px;top:198px;display:flex;align-items:center;gap:10px;color:#fff;font-family:'Oswald',sans-serif;font-weight:700;font-size:42px;line-height:1;white-space:nowrap}
  .coupon-number .phone-ring{width:36px;height:36px;border-width:3px}
  .coupon-number .phone-ring svg{width:18px;height:18px}
  .coupon-rule{position:absolute;left:204px;top:248px;width:286px;height:2px;background:#fff}
  .coupon-address{position:absolute;left:204px;top:254px;color:var(--ink);font-family:'Oswald',sans-serif;font-weight:500;font-size:14px;white-space:nowrap}

  /* emergency badge */
  .badge{position:absolute;display:flex;align-items:center;white-space:nowrap}
  .badge-pill{display:flex;align-items:center;background:var(--blue);border-radius:999px;color:#fff;font-family:'Oswald',sans-serif;font-weight:700;border:3px solid var(--orange-mid)}
  .badge-clock{border-radius:50%;background:linear-gradient(135deg,var(--orange),var(--yellow));display:flex;align-items:center;justify-content:center;border:3px solid #fff;flex:none}
  .badge-text{font-family:'Oswald',sans-serif;font-weight:700;font-style:italic}
  .badge-word{color:var(--blue-deep);display:block}
  .badge-strip{display:inline-block;color:#fff;background:linear-gradient(90deg,var(--orange),var(--yellow));transform:skewX(-12deg)}
  .badge-strip span{display:inline-block;transform:skewX(12deg)}

  .badge-small{left:232px;top:145px}
  .badge-small .badge-pill{font-size:24px;height:34px;padding-left:14px;gap:6px}
  .badge-small .badge-clock{width:38px;height:38px}
  .badge-small .badge-clock svg{width:20px;height:20px}
  .badge-small .badge-text{margin-left:10px;line-height:1.1}
  .badge-small .badge-word{font-size:16px;letter-spacing:5px}
  .badge-small .badge-strip{font-size:13px;padding:1px 8px}

  .badge-large{left:570px;top:418px}
  .badge-large .badge-pill{font-size:54px;height:72px;padding-left:24px;gap:10px}
  .badge-large .badge-clock{width:84px;height:84px}
  .badge-large .badge-clock svg{width:42px;height:42px}
  .badge-large .badge-text{margin-left:16px;line-height:1.05}
  .badge-large .badge-word{font-size:34px;letter-spacing:14px}
  .badge-large .badge-strip{font-size:30px;padding:2px 16px}

  .edge{position:absolute;left:0;bottom:0;width:100%;height:8px;background:linear-gradient(90deg,var(--orange),var(--orange-mid) 50%,var(--yellow))}
</style>
</head>
<body>
<main class="postcard">

  <div class="brand">
    <span class="brand-dot"></span>
    <span class="brand-name">PIPEWELL</span>
  </div>
  <div class="brand-tag">PLUMBING | DRAINAGE | GAS</div>

  <div class="contact">
    <div class="contact-item contact-email">
      <svg viewBox="0 0 24 24" fill="none" stroke="#fff" stroke-width="2"><rect x="3" y="5" width="18" height="14" rx="1"/><path d="M3 6l9 7 9-7"/></svg>
      hello@pipewell.com.au
    </div>
    <div class="contact-item contact-web">
      <svg viewBox="0 0 24 24" fill="none" stroke="#fff" stroke-width="2"><circle cx="12" cy="12" r="9"/><path d="M3 12h18M12 3c3 3 3 15 0 18M12 3c-3 3-3 15 0 18"/></svg>
      www.pipewell.com.au
    </div>
  </div>

  <div class="slogan-band"></div>
  <h1 class="slogan">TRY THE BEST,<br>FLUSH THE REST</h1>

  <p class="intro">
    <span class="name">PIPEWELL</span> would like to offer its fellow locals
    <span class="tag">$40 OFF</span> their next plumbing job.
    We pride ourselves in supplying the highest level of workmanship at the
    <span class="accent">most competitive prices.</span>
  </p>

  <div class="call-band"></div>
  <div class="call-tab">CALL US TODAY</div>
  <div class="call-number">
    <span class="phone-ring"><svg viewBox="0 0 24 24"><path fill="#1c9fd0" d="M6.6 10.8a15 15 0 006.6 6.6l2.2-2.2a1 1 0 011-.25 11.4 11.4 0 003.6.57 1 1 0 011 1V20a1 1 0 01-1 1A17 17 0 013 4a1 1 0 011-1h3.5a1 1 0 011 1c0 1.25.2 2.45.57 3.57a1 1 0 01-.25 1z"/></svg></span>
    0431 582 907
  </div>

  <section class="coupon">
    <div class="coupon-photo" role="img" aria-label="Photo of a smiling plumber in blue overalls holding a wrench beside a white service van"></div>
    <div class="coupon-bar"></div>
    <div class="coupon-offer">
      <div class="offer-amount">$40<small>OFF</small></div>
      <div class="offer-line">ON YOUR<br>NEXT<br>PLUMBING<br>JOB</div>
    </div>

    <div class="badge badge-small">
      <div class="badge-pill">24/7
        <span class="badge-clock"><svg viewBox="0 0 24 24" fill="none" stroke="#fff" stroke-width="2.2"><circle cx="12" cy="12" r="9"/><path d="M12 7v5l3 2"/></svg></span>
      </div>
      <div class="badge-text">
        <span class="badge-word">EMERGENCY</span>
        <span class="badge-strip"><span>PLUMBING SERVICE</span></span>
      </div>
    </div>

    <div class="coupon-number">
      <span class="phone-ring"><svg viewBox="0 0 24 24"><path fill="#1c9fd0" d="M6.6 10.8a15 15 0 006.6 6.6l2.2-2.2a1 1 0 011-.25 11.4 11.4 0 003.6.57 1 1 0 011 1V20a1 1 0 01-1 1A17 17 0 013 4a1 1 0 011-1h3.5a1 1 0 011 1c0 1.25.2 2.45.57 3.57a1 1 0 01-.25 1z"/></svg></span>
      0431 582 907
    </div>
    <div class="coupon-rule"></div>
    <div class="coupon-address">14 Harbour St Northgate 4013, Queensland</div>
  </section>

  <div class="badge badge-large">
    <div class="badge-pill">24/7
      <span class="badge-clock"><svg viewBox="0 0 24 24" fill="none" stroke="#fff" stroke-width="2"><circle cx="12" cy="12" r="9"/><path d="M12 7v5l3 2"/></svg></span>
    </div>
    <div class="badge-text">
      <span class="badge-word">EMERGENCY</span>
      <span class="badge-strip"><span>PLUMBING SERVICE</span></span>
    </div>
  </div>

  <div class="edge"></div>
</main>
</body>
</html>
```